Need a business card for a Construction and Remodeling company.
Our company logo is the fleur de lis design as thats the family crust that we use on our logos.
Heres the info it needs:

Brackmore Construction & Remodeling, LLC
Renovations * Restorations

Elwin R. Brackmore
845 North Quarry Road
Newtown Connecticut 06470
(203) 555.0182
CT LIC/REG: 418257

home owners, customers

```html
<!DOCTYPE html>
<html lang="en">
<head>
<meta charset="utf-8">
<title>Brackmore Construction &amp; Remodeling — Business Card</title>
<link rel="stylesheet" href="https://fonts.googleapis.com/css2?family=Cinzel:wght@400&family=Roboto+Condensed:wght@400&family=Roboto:wght@400;500&display=swap">
<style>
  :root {
    --page-bg: #ffffff;
    --card-light: #ffffff;
    --card-grey: #c9c9cb;
    --brand-orange: #e8731f;
    --ink-black: #0d0d0d;
    --panel-black: #141414;
    --panel-mid: #262626;
    --text-white: #f4f4f4;
  }
  * { margin: 0; padding: 0; box-sizing: border-box; }
  html, body {
    width: 1200px;
    height: 900px;
    overflow: hidden;
    background: var(--page-bg);
  }
  .canvas {
    position: relative;
    width: 1200px;
    height: 900px;
  }
  .business-card {
    position: absolute;
    left: 100px;
    top: 165px;
    width: 1000px;
    height: 570px;
    border-radius: 40px;
    overflow: hidden;
    background: linear-gradient(180deg, var(--card-grey) 0%, var(--card-light) 45%, var(--card-light) 54%);
  }
  .logo-mark {
    position: absolute;
    left: 450px;
    top: 40px;
    width: 100px;
    height: 100px;
  }
  .brand-block {
    position: absolute;
    left: 0;
    top: 160px;
    width: 1000px;
    text-align: center;
  }
  .brand-name {
    font-family: "Cinzel", serif;
    font-weight: 400;
    font-size: 66px;
    letter-spacing: 12px;
    color: var(--ink-black);
    line-height: 1;
  }
  .brand-tagline {
    margin-top: 6px;
    font-family: "Roboto Condensed", sans-serif;
    font-size: 28px;
    color: var(--brand-orange);
    line-height: 1.1;
  }
  .services-band {
    position: absolute;
    left: 0;
    top: 300px;
    width: 1000px;
    height: 30px;
    background: var(--brand-orange);
    display: flex;
    justify-content: space-around;
    align-items: center;
    padding: 0 40px;
  }
  .service {
    font-family: "Roboto", sans-serif;
    font-size: 19px;
    letter-spacing: 7px;
    color: var(--ink-black);
  }
  .contact-panel {
    position: absolute;
    left: 0;
    top: 330px;
    width: 1000px;
    height: 240px;
    background: radial-gradient(ellipse at 50% 30%, var(--panel-mid) 0%, var(--panel-black) 70%);
    text-align: center;
    font-family: "Roboto", sans-serif;
    color: var(--text-white);
    padding-top: 28px;
  }
  .person-name {
    font-weight: 500;
    font-size: 28px;
    color: var(--brand-orange);
    letter-spacing: 1px;
  }
  .phone {
    margin-top: 8px;
    font-size: 34px;
    letter-spacing: 1px;
  }
  .address {
    margin-top: 10px;
    font-size: 22px;
    line-height: 1.3;
  }
  .license {
    margin-top: 10px;
    font-size: 16px;
  }
</style>
</head>
<body>
<main class="canvas">
  <article class="business-card">
    <svg class="logo-mark" viewBox="0 0 100 100" role="img" aria-label="Company logo mark">
      <circle cx="50" cy="50" r="48" fill="var(--ink-black)"/>
    </svg>
    <header class="brand-block">
      <div class="brand-name">BRACKMORE</div>
      <div class="brand-tagline">Construction &amp; Remodeling, LLC</div>
    </header>
    <div class="services-band">
      <span class="service">RENOVATIONS</span>
      <span class="service">ADDITIONS</span>
      <span class="service">RESTORATIONS</span>
    </div>
    <section class="contact-panel">
      <div class="person-name">ELWIN R. BRACKMORE</div>
      <div class="phone">(203) 555.0182</div>
      <div class="address">845 North Quarry Road<br>Newtown Connecticut 06470</div>
      <div class="license">LIC/REG: 418257</div>
    </section>
  </article>
</main>
</body>
</html>
```